Brochure Design Project

We need a brochure design for an existing small Architectural Design company. The brochure needs to be in 2 pages in A4 format to be emailed to clients as a PDF. We have written the copy for the brochure, but we are very open to any suggestions you may have here. Our logo has been designed and is attached. This design will also need to be developed into a double sided "tri-fold" A4 brochure which will printed and distributed to perspective clients. We would like portrait pictures for the key staff next to each description, but do not have these as yet. Use any photos contained on our website www.plantrace.net.nz which you think will enhance the brochure. The brochure should reflect out website design and style.
Updates

Have changed the text file. Make sure the text file is called "profile kellow partners July 11".

Industry/Entity Type

It Company

Requirements
Must have
• Please use all the copy and logos provided. Design of brochure should fit with our existing logo. Must have a modern look with a high emphasis on design.
Nice to have
• As many photos as possible, without cluttering.
Should not have
• Must have a modern look with a high emphasis on design.

```html
<!DOCTYPE html>
<html lang="en">
<head>
<meta charset="utf-8">
<title>Kellow Partners – Brochure</title>
<link href="https://fonts.googleapis.com/css2?family=Questrial&family=Tinos&display=swap" rel="stylesheet">
<style>
:root{
  --lime:#a9c21b;
  --olive:#6f7d1c;
  --lime-soft:#b9cf4a;
  --ink:#1d1c1e;
  --slate:#59595b;
  --mist:#d9d9db;
  --paper:#f4f4f5;
  --white:#ffffff;
  --text-grey:#6b6b6e;
  --label:#a3a3a6;
}
*{margin:0;padding:0;box-sizing:border-box}
html,body{width:1200px;height:820px;overflow:hidden;background:var(--white)}
body{position:relative;font-family:"Questrial",Arial,sans-serif;color:var(--text-grey)}
.side-label{position:absolute;top:32px;font-size:18px;color:var(--label);letter-spacing:.5px}
.page{position:absolute;top:82px;width:478px;height:680px;background:var(--paper);overflow:hidden;box-shadow:0 1px 4px rgba(0,0,0,.25)}
.page--recto{left:86px}
.page--verso{left:625px;background:var(--white)}
.block{position:absolute}
.photo{position:absolute}
.green{background:var(--lime)}
.olive{background:var(--olive)}
.ink{background:var(--ink)}
.copy{position:absolute;font-size:8.6px;line-height:1.3;text-align:justify}
.h-small{font-size:9.5px;letter-spacing:1.6px;color:var(--lime);font-weight:bold}
.circle{position:absolute;border-radius:50%}

/* wordmark */
.wordmark{position:absolute;left:49px;top:92px;width:237px;height:96px;background:var(--ink);color:var(--white);padding:12px 0 0 20px}
.wordmark__name{font-size:44px;line-height:44px;letter-spacing:1px}
.wordmark__sub{font-size:11px;line-height:12px;letter-spacing:1px;text-align:right;padding-right:12px}
.wordmark__tag{font-size:7.5px;color:var(--lime);letter-spacing:.8px;margin:3px 0 0 60px}
.wordmark__contact{font-size:8.4px;letter-spacing:.6px;margin-top:5px}

.intro-title{position:absolute;left:75px;top:222px;color:var(--white);font-size:11px;letter-spacing:9px;font-weight:bold}
.intro-copy{left:75px;top:244px;width:333px;color:var(--text-grey)}
.intro-copy p+p{margin-top:10px}

.client-title{position:absolute;left:220px;top:367px;font-size:12.5px;letter-spacing:1.4px;color:var(--lime)}
.client-copy{left:220px;top:386px;width:245px;color:#9a9a9d}

.services-title{position:absolute;left:129px;top:498px;font-size:19px;letter-spacing:6px;line-height:21px;color:var(--ink)}
.services-title span{color:var(--lime-soft);-webkit-text-stroke:0}
.services-copy{left:147px;top:561px;width:285px;color:var(--white);font-size:8.8px;text-align:left}

/* verso */
.project-title{position:absolute;left:136px;top:34px;font-size:19px;letter-spacing:7px;line-height:22px}
.project-title .l1{color:var(--lime)}
.project-title .l2{color:var(--white)}
.col-copy{width:137px;color:var(--text-grey);font-size:8.2px}
.about-title{position:absolute;left:35px;top:350px;font-size:19px;letter-spacing:7px;line-height:21px;color:var(--ink)}
.about-copy{left:172px;top:337px;width:290px;color:#a8a8ab;font-size:8.5px}
.missing{position:absolute;font-family:"Tinos",serif;color:var(--white);font-size:13px;white-space:nowrap}
.staff-role{position:absolute;font-size:6.4px;color:var(--lime);font-weight:bold}
.staff-name{font-size:7.6px;color:var(--lime);font-weight:bold}
.staff-copy{position:absolute;font-size:7.4px;line-height:1.2;color:var(--text-grey)}
.footer-contact{position:absolute;left:184px;top:633px;font-size:5.2px;line-height:1.35;color:var(--lime);font-weight:bold}
.footer-mark{position:absolute;left:347px;top:618px;width:127px;height:44px;color:var(--white);padding:4px 0 0 14px}
.footer-mark .n{font-size:19px;line-height:19px}
.footer-mark .s{font-size:6px;text-align:right;padding-right:6px}
.footer-mark .t{font-size:4px;color:var(--lime);text-align:right;padding-right:6px}
.footer-mark .c{font-size:4.6px;text-align:right;padding-right:6px;margin-top:2px}
</style>
</head>
<body>

<div class="side-label" style="left:88px">recto</div>
<div class="side-label" style="left:618px">verso</div>

<!-- RECTO -->
<section class="page page--recto">
  <div class="block green" style="left:0;top:0;width:231px;height:90px"></div>
  <div class="block olive" style="left:0;top:90px;width:231px;height:122px"></div>
  <div class="photo" role="img" aria-label="Render of a two-storey contemporary house with balconies under a blue sky" style="left:231px;top:0;width:247px;height:212px;background:linear-gradient(180deg,#8fb4d8 0%,#aec6db 45%,#6d7266 70%,#4e5a3c 100%)"></div>

  <div class="wordmark">
    <div class="wordmark__name">kellow</div>
    <div class="wordmark__sub">partners ltd</div>
    <div class="wordmark__tag">ARCHITECTURAL DESIGN</div>
    <div class="wordmark__contact">P 07 555 0142 &nbsp;-&nbsp; www.plantrace.net</div>
  </div>

  <div class="block" style="left:49px;top:212px;width:380px;height:147px;background:var(--mist)"></div>
  <div class="block" style="left:0;top:212px;width:49px;height:92px;background:var(--lime-soft)"></div>

  <div class="intro-title">Kellow Partners Limited</div>
  <div class="copy intro-copy">
    <p>Kellow Partners Limited is an Architectural Design practise based in Hamilton and provides Architectural and Development consultation services in the Waikato, Coromandel, Auckland and Bay of Plenty regions and is recognised for providing innovative design solutions to many satisfied clients.</p>
    <p>The architectural character of each building we design is unique because every design is a response to several factors including climate, views, topography, site context, functional program and the aesthetic sensibilities of our clients, infused with our own architectural vision.</p>
  </div>

  <div class="photo" role="img" aria-label="Photo of a modern white house with a curved roof" style="left:0;top:359px;width:212px;height:70px;background:linear-gradient(180deg,#6e98c4 0%,#b9c6cf 55%,#4e5c3e 100%)"></div>
  <div class="block ink" style="left:212px;top:357px;width:266px;height:113px"></div>
  <div class="circle" style="left:212px;top:337px;width:50px;height:40px;background:var(--ink);border:6px solid var(--white);border-bottom:none;border-radius:30px 30px 0 0"></div>
  <div class="client-title">CLIENT FOCUSED</div>
  <div class="copy client-copy">Right from the early stages of the design process the Client is an integral part of the team. By listening to our clients we are able to deliver design solutions which meet their individual requirements and allows us to draw on our years of experience to create designs which are exciting, distinctive and cost effective.</div>

  <div class="photo" role="img" aria-label="Photo of a rendered two-storey villa" style="left:25px;top:435px;width:98px;height:55px;background:linear-gradient(180deg,#a9c3dd 0%,#d7d2c6 60%,#9a9688 100%)"></div>
  <div class="photo" role="img" aria-label="Photo of a white modern building against blue sky" style="left:125px;top:435px;width:87px;height:55px;background:linear-gradient(180deg,#5f8fc2 0%,#c9d0d5 65%,#8c9287 100%)"></div>

  <div class="block green" style="left:125px;top:492px;width:353px;height:170px"></div>
  <div class="circle green" style="left:139px;top:472px;width:42px;height:42px"></div>
  <div class="circle green" style="left:100px;top:567px;width:42px;height:42px"></div>
  <div class="services-title"><span>OUR</span><br>SERVICES</div>
  <div class="copy services-copy">• Site inspection, assessment and feasibility • Conceptual design. • Secondary Consultant liaison and management • 3D Modelling and Renders • Resource Consent Documentation • Developed design • Construction documentation • Tender Process Management • Site observation • Contract administration • Green technology Analysis.</div>

  <div class="block ink" style="left:0;top:662px;width:431px;height:16px"></div>
</section>

<!-- VERSO -->
<section class="page page--verso">
  <div class="photo" role="img" aria-label="Photo of a contemporary house with a dark garage door and hedging" style="left:0;top:0;width:159px;height:196px;background:linear-gradient(160deg,#2f3438 0%,#6c7378 50%,#b9bcb9 80%,#4f6a36 100%)"></div>
  <div class="block" style="left:159px;top:0;width:162px;height:70px;background:var(--slate)"></div>
  <div class="block" style="left:136px;top:0;width:23px;height:70px;background:rgba(40,40,42,.55)"></div>
  <div class="circle" style="left:98px;top:182px;width:40px;height:28px;background:#4f7a2e;border-radius:0 0 20px 20px"></div>
  <div class="circle" style="left:150px;top:136px;width:14px;height:28px;background:var(--ink);border-radius:0 14px 14px 0"></div>
  <div class="project-title"><div class="l1">PROJECT</div><div class="l2">EXPERIENCE</div></div>

  <div class="h-small" style="position:absolute;left:171px;top:84px">RESIDENTIAL</div>
  <div class="copy col-copy" style="left:171px;top:97px">Residential projects require a unique blend of creativity and client consideration. We have a vast range of experience in designing and documenting new homes, house relocations and house alterations for many satisfied clients, from simple 2 bedroom units to large multi level dwellings.</div>
  <div class="h-small" style="position:absolute;left:171px;top:206px">REMEDIAL</div>
  <div class="copy col-copy" style="left:171px;top:218px;height:87px;overflow:hidden">Remedial work is an increasing body of work as a result of New Zealand's leaky building crisis and is fast becoming a large part of the New Zealand Building Industry landscape. We have the experience and contacts to work in with and if necessary lead the team.</div>

  <div class="h-small" style="position:absolute;left:317px;top:84px">MULTI-UNIT RESIDENTIAL:</div>
  <div class="copy col-copy" style="left:317px;top:97px;width:133px">Having successfully completed the design and documentation for over 150 Multi-Unit residential developments, we have demonstrated that we are well resourced to offer a range of skills for any development of this nature. With two national design awards for this type of design, we can rightly claim to be experts in this field.</div>
  <div class="h-small" style="position:absolute;left:317px;top:217px">COMMERCIAL:</div>
  <div class="copy col-copy" style="left:317px;top:229px;width:133px">Good design adds value to any project, especially Commercial projects. As the design team leader, Kellow Partners has a track record of leading exciting and dynamic commercial developments.</div>

  <div class="photo" role="img" aria-label="Photo of a white commercial building with a pitched entrance canopy" style="left:0;top:204px;width:159px;height:105px;background:linear-gradient(180deg,#3d6fb0 0%,#9fb6cf 45%,#e2ddd2 70%,#6e7a55 100%)"></div>

  <div class="block green" style="left:0;top:309px;width:161px;height:127px"></div>
  <div class="block ink" style="left:161px;top:309px;width:317px;height:147px"></div>
  <div class="circle" style="left:148px;top:365px;width:24px;height:30px;background:var(--ink);border-radius:15px 0 0 15px"></div>
  <div class="about-title">ABOUT<br>US</div>
  <div class="copy about-copy">The staff at Kellow Partners are all industry professionals with a high level of training. Ongoing professional development is a big part of the company philosophy, which keeps us up to date with developing trends, construction techniques and technical developments within the industry. We make optimal use of technology to reduce design time and streamline project delivery. Internal peer reviews are completed prior to the issue of each stage to ensure quality control.</div>

  <div class="photo" role="img" aria-label="Staff portrait placeholder beside an apartment building" style="left:29px;top:421px;width:133px;height:108px;background:linear-gradient(180deg,#c7d3dd 0%,#8c9ba3 50%,#2f4b2c 100%)"></div>
  <div class="circle" style="left:69px;top:410px;width:34px;height:22px;background:var(--ink);border-radius:17px 17px 0 0"></div>
  <div class="missing" style="left:35px;top:505px">Photo missing</div>
  <div class="photo" role="img" aria-label="Staff portrait placeholder beside apartment balconies" style="left:162px;top:456px;width:95px;height:91px;background:linear-gradient(180deg,#dfe4e6 0%,#a3adb0 50%,#36542f 100%)"></div>
  <div class="circle" style="left:190px;top:448px;width:30px;height:18px;background:var(--ink);border-radius:0 0 15px 15px"></div>
  <div class="missing" style="left:172px;top:480px">Photo missing</div>
  <div class="photo" role="img" aria-label="Staff portrait placeholder beside palm fronds and building" style="left:366px;top:529px;width:88px;height:86px;background:linear-gradient(180deg,#6e97c5 0%,#c9d3d8 50%,#3b5a34 100%)"></div>
  <div class="missing" style="left:370px;top:552px">Photo missing</div>

  <div class="staff-role" style="left:29px;top:533px">Managing Director:</div>
  <div class="staff-copy" style="left:29px;top:557px;width:130px;text-align:justify"><span class="staff-name">Martin Kellow, NZCD (Arch).</span><br>As the lead designer and team leader, Martin has 20 years experience in architectural design and contract management. He has a Design 2 Architectural Design license and is registered with the Department of Building and Housing and is a member of the NZ Design Practice Guild.</div>

  <div class="staff-copy" style="left:262px;top:476px;width:200px"><span class="staff-name">Liam Corrigan, Dip.Arch</span><br>Liam has over 10 years experience locally and overseas in design, Architectural Cad Draughting and project management.</div>
  <div class="staff-role" style="left:262px;top:534px">Projects Manager</div>

  <div class="staff-copy" style="left:237px;top:563px;width:128px"><span class="staff-name">Rhys Tamaki, Dip.Arch</span><br>3 years experience in Architectural Cad Draughting and Design.</div>
  <div class="staff-role" style="left:290px;top:604px">CAD draughtsperson</div>

  <div class="block ink" style="left:180px;top:615px;width:298px;height:48px"></div>
  <div class="footer-contact">PO Box 40210, Hamilton 3240, New Zealand<br>Ph: 64 7 5550142 - Fax: 64 7 5550143 - Mob: 021555086<br>email: admin@plantrace.net.nz<br>Website: &nbsp; www.plantrace.net.nz</div>
  <div class="footer-mark">
    <div class="n">kellow</div>
    <div class="s">partners ltd</div>
    <div class="t">ARCHITECTURAL DESIGN</div>
    <div class="c">P 07 555 0142 · www.plantrace.net</div>
  </div>
  <div class="block ink" style="left:0;top:663px;width:431px;height:15px"></div>
  <div class="block green" style="left:445px;top:668px;width:33px;height:10px"></div>
</section>

</body>
</html>
```